Australian Online Training Organisation needs a Website Design

We need a Web Design ideally using a Wordpress Divi template which will represent an Australian Online Training Company.

(Harlow Net Learning)

The website will represent a range of short courses with an emphasis on business, zentrosoft, leadership etc.

The website will 'shell out' to the third party portal where 'bookings' occur. I am imaging a fantastic looking web design with perhaps 5-6 pages.

I am wondering if a selection of courses including the below list can be incorporated?

The variety of courses include :

Workplace Safety
Sales Training
Leadership
Process Management
Problem Solving
Project Management
Business Planning
Meetings and Events
Emotional Intelligence
Human Resources
Administrative Essentials
Customer Service
Career Development
Conflict Resolution
Train the Trainer
Supervisors and Managers
Internet marketing
Communications
Team Building
Marketing
Finance
Writing
Job Search Skills
Public Speaking
Negotiation Skills
Talent Management
Zentrosoft Deskline 2016
ZDC Preparation for Office 2010
Office 2013
Office 2010
Upgrading to Office 2010
Computer Fundamentals
Upgrading to Office 2007
Office 2003
Office 2002
Pavra Suite X3
Core Essentials
Office 2007

Thank you so much for all of the amazing designs we received. We were so happy with so many elements that it was very hard to choose. Our top two were very hard to decide upon but we look forward to working more with both of these talents into the future. Thank you again.

Target Market(s)

Professionals, students and workers who would like to improve their skills with online training in over 500 + courses -

Industry/Entity Type

It Company

Number of Pages Required

5+ page

Font styles to use
Sans Serif

Colors
3276b5
faa54b
0355a3
fac994

Requirements
Must have
• Ideally would use Wordpress theme (Divi for example or other)
• Very smart front end
• Will upload logo soon
• (Harlow Net Learning)
• harlownetlearning.edu.au
• Graphics of 'people' pretty important - with a variety of ages.
Nice to have
• Interesting page
• National presence
• A bit University looking
• Professional
• Graphics of people
• Blog
• Graphics of people
• Age range from job seekers, to business folk, etc

```html
<!DOCTYPE html>
<html lang="en">
<head>
<meta charset="utf-8">
<title>Harlow Net Learning</title>
<link rel="stylesheet" href="https://fonts.googleapis.com/css2?family=Montserrat:wght@400;600;700&family=Open+Sans:wght@400;600;700&display=swap">
<style>
:root{
  --orange:#f7941d;
  --orange-soft:#faa54b;
  --peach:#fac994;
  --blue:#0355a3;
  --ink:#333333;
  --muted:#777777;
  --light:#f2f2f2;
  --dark:#333333;
  --white:#ffffff;
}
*{box-sizing:border-box;margin:0;padding:0}
html,body{width:1200px;height:3341px;overflow:hidden}
body{background:var(--white);font-family:"Open Sans",Arial,sans-serif;color:var(--ink);position:relative}
h1,h2,h3,h4,.brand{font-family:"Montserrat",Arial,sans-serif}

/* header */
.site-header{position:absolute;left:150px;top:0;width:900px;height:125px}
.brand{position:absolute;left:14px;top:22px;display:flex;align-items:center;gap:10px;color:var(--blue);font-weight:700;font-size:22px}
.brand .mark{width:34px;height:34px;border-radius:50%;background:var(--blue)}
.brand small{display:block;font-size:11px;font-weight:600;color:var(--muted);letter-spacing:1px}
.phone{position:absolute;left:645px;top:38px;font-family:"Montserrat",sans-serif;font-weight:700;font-size:22px;display:flex;align-items:center;gap:8px;white-space:nowrap}
.login{position:absolute;left:838px;top:43px;font-size:13px;color:var(--orange);display:flex;gap:6px;align-items:center}
.nav{position:absolute;right:0;top:78px;display:flex;gap:4px;font-size:12px;font-weight:600;white-space:nowrap}
.nav a{color:var(--ink);text-decoration:none;padding:5px 10px;border-radius:14px;white-space:nowrap}
.nav a.active{background:var(--orange);color:var(--white)}

/* hero */
.hero{position:absolute;left:150px;top:125px;width:900px;height:546px;background:
  radial-gradient(ellipse at 28% 45%,rgba(70,74,80,.55) 0%,rgba(70,74,80,0) 45%),
  linear-gradient(100deg,#7d8389 0%,#b9bcba 40%,#e4e1da 68%,#b9b6ae 100%)}
.hero-text{position:absolute;left:475px;top:168px;color:var(--white)}
.hero-text h1{font-size:56px;line-height:60px;font-weight:600;white-space:nowrap}
.hero-text p{font-size:17px;line-height:22px;margin-top:6px;width:350px}
.hero-search{position:absolute;left:479px;top:340px;width:352px;height:37px;background:var(--orange);border-radius:19px;color:var(--white);font-size:13px;padding:10px 20px;display:flex;justify-content:space-between;align-items:center}
.hero-tab{position:absolute;right:0;top:240px;width:0;height:0;border-top:26px solid transparent;border-bottom:26px solid transparent;border-right:22px solid var(--white)}

/* welcome */
.eyebrow{font-family:"Montserrat",sans-serif;font-weight:700;font-size:14px;text-align:center;letter-spacing:1px}
.section-title{font-family:"Montserrat",sans-serif;font-weight:700;color:var(--orange);font-size:24px;text-align:center}
.rule{width:40px;height:2px;background:var(--orange);margin:8px auto 0}
.welcome{position:absolute;left:150px;top:722px;width:900px;text-align:center}
.welcome p{font-size:13px;line-height:21px;color:#555;width:800px;margin:22px auto 0}

/* why */
.why{position:absolute;left:150px;top:1055px;width:900px;height:354px;background:linear-gradient(90deg,rgba(247,148,29,.97),rgba(250,165,75,.94)),#e98a1a;color:var(--white)}
.why .eyebrow{margin-top:48px;color:var(--white)}
.why .rule{background:var(--white)}
.why-cols{position:absolute;top:123px;left:40px;display:flex;gap:30px}
.why-col{width:255px;display:flex;gap:12px}
.why-col .icon{flex:none;width:58px;height:58px;border-radius:50%;background:var(--ink);display:flex;align-items:center;justify-content:center}
.why-col h4{font-size:14px;font-weight:700;margin-bottom:6px}
.why-col p{font-size:12.5px;line-height:18px}

/* clients */
.clients{position:absolute;left:150px;top:1414px;width:900px;height:106px;background:var(--light);display:flex;align-items:center;justify-content:space-around;padding:0 40px}
.clients span{font-family:"Montserrat",sans-serif;font-weight:700;font-size:22px;color:#a8a8a8}
.clients .arrow{position:absolute;top:38px;font-size:20px;color:var(--ink)}

/* courses */
.courses-head{position:absolute;left:150px;top:1574px;width:900px}
.courses-head .section-title{font-size:24px;margin-top:4px}
.course{position:absolute;width:217px}
.course .thumb{height:147px}
.course h3{font-size:14px;font-weight:700;margin-top:14px;white-space:nowrap}
.course .meta{font-size:11px;color:var(--muted);margin-top:8px}
.course .price{font-size:11px;color:var(--muted);margin-top:6px;display:flex;align-items:center;gap:6px}
.course .price b{color:var(--orange)}

/* blog */
.blog{position:absolute;left:150px;top:2227px;width:900px;height:468px;background:var(--orange)}
.blog .eyebrow{color:var(--ink);margin-top:44px}
.blog .rule{background:var(--white)}
.post{position:absolute;top:112px;width:234px;color:var(--white)}
.post .thumb{height:181px;position:relative}
.post .date{position:absolute;left:0;bottom:0;width:64px;height:58px;background:var(--ink);color:var(--white);font-family:"Montserrat",sans-serif;font-weight:700;font-size:14px;line-height:18px;padding:10px}
.post h3{font-size:15px;font-weight:700;margin-top:14px}
.post p{font-size:11px;line-height:15px;margin-top:6px;opacity:.95}

/* review */
.review{position:absolute;left:150px;top:2745px;width:900px;height:320px;text-align:center}
.review .eyebrow{color:var(--ink)}
.avatars{position:absolute;left:0;top:105px;width:900px;height:80px}
.avatar{position:absolute;border-radius:50%}
.review h4{position:absolute;left:0;top:224px;width:900px;font-size:14px;font-weight:700}
.review .role{position:absolute;left:0;top:244px;width:900px;font-size:12px;color:var(--muted)}
.review .quote{position:absolute;left:0;top:293px;width:900px;font-size:13px;color:var(--ink)}
.review .qmark{position:absolute;top:280px;font-family:Georgia,serif;font-size:40px;line-height:40px;color:#ccc}

/* footer */
.site-footer{position:absolute;left:150px;top:3090px;width:900px;height:251px;background:var(--dark);color:var(--white)}
.site-footer h4{font-size:13px;font-weight:700;letter-spacing:.5px}
.f-col{position:absolute;top:40px}
.f-col p{font-size:12px;line-height:18px;margin-top:10px}
.subscribe{margin-top:24px;width:265px;height:36px;border-radius:18px;background:var(--white);color:#999;font-size:12px;padding:10px 18px;display:flex;justify-content:space-between;align-items:center}
.copyright{position:absolute;left:0;bottom:22px;width:900px;text-align:center;font-size:10px;color:#aaa;border-top:1px solid #4a4a4a;padding-top:16px}
</style>
</head>
<body>

<header class="site-header">
  <div class="brand"><span class="mark"></span><div>Harlow Net Learning<small>ONLINE TRAINING</small></div></div>
  <div class="phone">
    <svg width="18" height="18" viewBox="0 0 24 24"><path d="M6.6 10.8c1.4 2.8 3.8 5.1 6.6 6.6l2.2-2.2c.3-.3.7-.4 1-.2 1.1.4 2.3.6 3.6.6.6 0 1 .4 1 1V20c0 .6-.4 1-1 1C10.6 21 3 13.4 3 4c0-.6.4-1 1-1h3.5c.6 0 1 .4 1 1 0 1.3.2 2.5.6 3.6.1.3 0 .7-.2 1z" fill="#333"/></svg>
    1800 555 014
  </div>
  <div class="login">
    <svg width="16" height="16" viewBox="0 0 16 16"><circle cx="8" cy="8" r="8" fill="#333"/><circle cx="8" cy="6" r="3" fill="#fff"/><path d="M3 13c1-3 9-3 10 0" fill="#fff"/></svg>
    Login
  </div>
  <nav class="nav">
    <a class="active">Home</a><a>About Us</a><a>Courses</a><a>Support and Resources</a><a>For Employers</a><a>Testimonials</a>
  </nav>
</header>

<section class="hero" role="img" aria-label="Photo of a young professional working at a laptop in a bright office">
  <div class="hero-text">
    <h1>We over 600<br>well priced</h1>
    <p>accessable short courses in a variety of skill sets online. Directly to you</p>
  </div>
  <div class="hero-search">
    <span>Search 500 + courses</span>
    <svg width="15" height="15" viewBox="0 0 16 16"><circle cx="6.5" cy="6.5" r="5" stroke="#fff" stroke-width="2" fill="none"/><path d="M10 10l5 5" stroke="#fff" stroke-width="2"/></svg>
  </div>
  <div class="hero-tab"></div>
</section>

<section class="welcome">
  <div class="eyebrow">WELCOME TO</div>
  <div class="section-title" style="font-size:22px;margin-top:4px">Harlow Net Learning</div>
  <div class="rule"></div>
  <p>Harlow Net Learning is one of Australia's leading provider of flexible and affordable online continuing professional development programs, with over 600 online courses now available. Our range of self-paced online courses are delivered completely online via our e-learning system 24/7.<br>
  We offer a range of popular online courses in accounting, finance, bookkeeping, management, marketing, information technology, project management and more. Our online courses are industry relevant and are designed to help you achieve your career goals.<br>
  Harlow specialise in online Zentrosoft product training - preffect.<br>
  Studying online allows you to balance study with your existing work and home life commitments. With Harlow Online you can learn in your own space from work, at home or anywhere you have an internet connection.<br>
  Our All-Inclusive Fee Guarantee ensures that you receive all course materials, 12 months' e-learning access with no more to pay. Free extensions are also available if you need extra time to complete your course.</p>
</section>

<section class="why" aria-label="Why Harlow Online">
  <div class="eyebrow">WHY HARLOW ONLINE</div>
  <div class="rule"></div>
  <div class="why-cols">
    <div class="why-col">
      <div class="icon"><svg width="28" height="28" viewBox="0 0 24 24"><path d="M2 10h4v11H2zM8 21h9c.8 0 1.5-.5 1.8-1.2l2.9-6.8c.2-.5.3-.9.3-1.4V10c0-1.1-.9-2-2-2h-6l1-4.6c.1-.6-.1-1.2-.5-1.6L13.4 1 8 6.6z" fill="#f7941d"/></svg></div>
      <div><h4>FLEXIBLE</h4><p>Harlow provide an online learning platform which fits your lifestyle and work commitments. You study anywhere, anytime!</p></div>
    </div>
    <div class="why-col">
      <div class="icon"><svg width="28" height="28" viewBox="0 0 24 24"><path d="M3 3h9l9 9-9 9-9-9z" fill="#f7941d"/><circle cx="8" cy="8" r="1.8" fill="#333"/></svg></div>
      <div><h4>VALUE</h4><p>Our innovative online learning approach allows us to deliver excellence training in over 600 industry endorsed courses at affordable prices with no hidden extras. Courses may be tax deductable - check with your Tax Agent today!</p></div>
    </div>
    <div class="why-col">
      <div class="icon"><svg width="28" height="28" viewBox="0 0 24 24"><rect x="10" y="2" width="4" height="6" fill="#f7941d"/><path d="M8 9h8l1 13H7z" fill="#f7941d"/></svg></div>
      <div><h4>EXPERIENCE</h4><p>Harlow is one of Australia's largest and leading providers of training services in nationally.</p></div>
    </div>
  </div>
</section>

<section class="clients" aria-label="Client companies">
  <span class="arrow" style="left:14px">&#8249;</span>
  <span>Brookvale</span><span>Coralby</span><span>Swiftlane</span>
  <svg width="40" height="40" viewBox="0 0 40 40"><circle cx="20" cy="20" r="17" fill="#c4c4c4"/></svg>
  <span>Telvio</span><span>Buildmart</span>
  <span class="arrow" style="right:14px">&#8250;</span>
</section>

<section class="courses-head">
  <div class="eyebrow">THE VARIETY OF</div>
  <div class="section-title">courses</div>
  <div class="rule"></div>
</section>

<article class="course" style="left:150px;top:1693px"><div class="thumb" role="img" aria-label="Photo of safety helmets" style="background:radial-gradient(circle at 60% 55%,#f6c820 0%,#e0a815 35%,#2f3d4a 80%)"></div><h3>Workplace Safety</h3><div class="meta">Start on June, 2016 | 3 courses</div><div class="price">Enrol now | <b>$99.00</b></div></article>
<article class="course" style="left:376px;top:1693px"><div class="thumb" role="img" aria-label="Photo of a sales team at a desk" style="background:linear-gradient(135deg,#8fa8bd,#d7d9d6 55%,#efe9e0)"></div><h3>Sales Training</h3><div class="meta">Start on June, 2016 | 3 courses</div><div class="price">Enrol now | <b>$99.00</b></div></article>
<article class="course" style="left:601px;top:1693px"><div class="thumb" role="img" aria-label="Photo of one green figure leading red figures" style="background:radial-gradient(circle at 40% 30%,#6f9a3a 0%,#c9c0b5 25%,#b3362d 85%)"></div><h3>Leadership</h3><div class="meta">Start on June, 2016 | 3 courses</div><div class="price">Enrol now | <b>$99.00</b></div></article>
<article class="course" style="left:830px;top:1693px"><div class="thumb" role="img" aria-label="Photo of hands planning a process on paper" style="background:linear-gradient(135deg,#f4f1ec,#e9d9bf 55%,#d9a35a)"></div><h3>Process Management</h3><div class="meta">Start on June, 2016 | 3 courses</div><div class="price">Enrol now | <b>$99.00</b></div></article>

<article class="course" style="left:150px;top:1940px"><div class="thumb" role="img" aria-label="Photo of a project planning chart" style="background:linear-gradient(135deg,#5a2e22,#c02c2c 60%,#8e1f1f)"></div><h3>Project Management</h3><div class="meta">Start on June, 2016 | 3 courses</div><div class="price">Enrol now | <b>$99.00</b></div></article>
<article class="course" style="left:376px;top:1940px"><div class="thumb" role="img" aria-label="Business plan sketch on a chalkboard" style="background:radial-gradient(circle at 55% 40%,#2d7ea8 0%,#1d5a7a 40%,#12324a 90%)"></div><h3>Business Planning</h3><div class="meta">Start on June, 2016 | 3 courses</div><div class="price">Enrol now | <b>$99.00</b></div></article>
<article class="course" style="left:601px;top:1940px"><div class="thumb" role="img" aria-label="Photo of an event hall set for a meeting" style="background:linear-gradient(160deg,#e2d3b5,#b89868 55%,#7a5a3a)"></div><h3>Meetings and Events</h3><div class="meta">Start on June, 2016 | 3 courses</div><div class="price">Enrol now | <b>$99.00</b></div></article>
<article class="course" style="left:830px;top:1940px"><div class="thumb" role="img" aria-label="Photo of a tablet showing office software" style="background:radial-gradient(circle at 50% 50%,#e9eef4 0%,#b9c6d4 45%,#6f8299 95%)"></div><h3>Zentrosoft Deskline 2016</h3><div class="meta">Start on June, 2016 | 3 courses</div><div class="price">Enrol now | <b>$99.00</b></div></article>

<section class="blog" aria-label="Blog">
  <div class="eyebrow">BLOG</div>
  <div class="rule"></div>
  <article class="post" style="left:78px"><div class="thumb" role="img" aria-label="Photo of hands typing on a laptop" style="background:linear-gradient(135deg,#f0f3f5,#c9d0d6 50%,#8d99a3)"><div class="date">18th<br>June</div></div><h3>Etiam sit amet</h3><p>Ultricies nec, pellentesque eu, pretium quis, sem. Nulla consequat massa quis enim. Donec pede justo, fringilla vel, aliquet nec, vulputate eget.</p></article>
  <article class="post" style="left:337px"><div class="thumb" role="img" aria-label="Photo of a team reviewing documents" style="background:linear-gradient(135deg,#e3d6c4,#a48f78 55%,#6a5a4a)"><div class="date">18th<br>June</div></div><h3>Phasellus viverra</h3><p>Ut libero venenatis faucibus. Nullam quis ante. Etiam sit amet orci eget eros faucibus tincidunt. Duis leo. Sed fringilla mauris sit amet nibh.</p></article>
  <article class="post" style="left:596px"><div class="thumb" role="img" aria-label="Illustration of connected people icons" style="background:radial-gradient(circle at 50% 45%,#5c92d4 0%,#3a6fb5 45%,#1f4e8c 95%)"><div class="date">18th<br>June</div></div><h3>Donec pede justo</h3><p>Aenean massa. Cum sociis natoque penatibus et magnis dis parturient montes, nascetur ridiculus mus. Donec quam felis, ultricies nec.</p></article>
</section>

<section class="review" aria-label="Customer review">
  <div class="eyebrow">CUSTOMER REVIEW</div>
  <div class="rule"></div>
  <div class="avatars">
    <div class="avatar" role="img" aria-label="Customer portrait" style="left:340px;top:22px;width:34px;height:34px;background:#bdbdbd"></div>
    <div class="avatar" role="img" aria-label="Customer portrait" style="left:411px;top:0;width:78px;height:78px;background:linear-gradient(135deg,#8a6b58,#3a2a24)"></div>
    <div class="avatar" role="img" aria-label="Customer portrait" style="left:526px;top:22px;width:34px;height:34px;background:#bdbdbd"></div>
  </div>
  <h4>NADIA VERHOEVEN</h4>
  <div class="role">Global Knowledge Officer</div>
  <span class="qmark" style="left:248px">&ldquo;</span>
  <div class="quote">You have a great product and I'm glad our paths crossed</div>
  <span class="qmark" style="left:632px">&rdquo;</span>
</section>

<footer class="site-footer">
  <div class="f-col" style="left:45px">
    <h4>SUBSCRIBE TO NEWSLETTER</h4>
    <div class="subscribe"><span>Email Address</span>
      <svg width="22" height="16" viewBox="0 0 22 16"><rect x="1" y="1" width="20" height="14" fill="none" stroke="#333" stroke-width="1.6"/><path d="M1 1l10 8 10-8M1 15l7-6M21 15l-7-6" fill="none" stroke="#333" stroke-width="1.6"/></svg>
    </div>
  </div>
  <div class="f-col" style="left:407px">
    <h4 style="color:var(--orange)">HARLOW NET LEARNING</h4>
    <p>ABN 00 000 000 000 Head Office,<br>27 Kestrel Rise,<br>Innovation Park,<br>Ardley 6990 PO Box 4410<br>Ardley DC 6990</p>
  </div>
  <div class="f-col" style="left:733px">
    <h4 style="color:var(--orange)">FREECALL</h4>
    <p>1800 555 014</p>
  </div>
  <div class="copyright">&copy;2016 harlownetlearning.edu.au. All Rights Reserved</div>
</footer>

</body>
</html>
```